Website Design

I require a website to be built around a CMS for a commercial client, an SME in the construction industry
I am happy to approach this 2 ways - either a full site redesign and build around a well known CMS by the successful candidate. Or a page template designed which I can then duplicate and use with a light CMS - I have enough coding experience to implement this myself.
I require a html/css file as the final piece of work,
Updates
Hi,
This is the site to be redesigned:
http://www.vexbornplatforms.co.uk/
As you can see it is quite dated.
The design should be quite focused on the images and photos of the products.
2 designs which were reject can be seen here:
vexbornplatforms.tundrapixel.co.uk
vexbornplatforms2.tundrapixel.co.uk
This is the clients main competitor: http://www.quillrigging.com/ - They are keen to have a site which is 'better' than this one.
Hope this info helps. The site will include a lightbox gallery to focus on products, please bare this is mind when submitting your designs.
Reason: Need a higher number of designs to take to the client.
We are happy just to accept PSD designs if you believe the budget is too low for a HTML design. Please get in touch if you require more info.
Please can you use the customers logo from the website in designs. Thanks
Reason: Need more designers!
Target Market(s)
Industrial/Construction Sector
Industry/Entity Type
Construction
Requirements
Must have
- final design must be in html

```html
<!DOCTYPE html>
<html lang="en">
<head>
<meta charset="utf-8">
<title>Vexborn Platforms Ltd</title>
<link href="https://fonts.googleapis.com/css2?family=Asap:wght@400;500&display=swap" rel="stylesheet">
<style>
:root{
  --header:#1f2227;
  --stage:#4b5361;
  --page:#e4e5e7;
  --panel:#6b7483;
  --frame:#a8afba;
  --photo-dark:#3e4556;
  --photo-light:#8b96aa;
  --heading:#c9d3e2;
  --text:#ffffff;
  --nav:#c3c8cf;
  --footer:#3b424d;
  --thumb-border:#d9dde2;
}
*{margin:0;padding:0;box-sizing:border-box}
html,body{width:1000px;height:1200px;overflow:hidden}
body{position:relative;font-family:"Asap",sans-serif;background:var(--page);color:var(--text)}
.stage-band{position:absolute;left:0;top:102px;width:1000px;height:403px;background:var(--stage)}
.site-header{position:absolute;left:0;top:0;width:1000px;height:102px;background:var(--header)}
.brand{position:absolute;left:54px;top:16px;font-size:29px;font-weight:500;letter-spacing:1px;color:#fff;text-transform:uppercase}
.main-nav{position:absolute;left:142px;top:66px;display:flex}
.main-nav a{display:block;font-size:16px;color:var(--nav);text-decoration:none;height:29px;line-height:29px;padding:0 16px;margin-right:7px}
.main-nav a.active{background:linear-gradient(#8a939e,#545c67);color:#fff;border-radius:6px;border:1px solid #a5adb7}
.slider{position:absolute;left:46px;top:110px;width:909px;height:418px;background:var(--frame);box-shadow:0 8px 10px rgba(0,0,0,.45)}
.slider .photo{position:absolute;left:16px;top:16px;width:877px;height:386px;background:linear-gradient(180deg,var(--photo-light),var(--photo-dark) 70%,#2c313c)}
.dots{position:absolute;left:464px;top:538px;display:flex;gap:8px}
.dots span{width:12px;height:12px;background:#d4d8de;border:1px solid #9aa2ad}
.dots span.on{background:#3c434e}
.panel{position:absolute;left:46px;top:528px;width:909px;height:610px;background:var(--panel)}
h2{position:absolute;font-size:24px;font-weight:400;color:var(--heading)}
.intro{position:absolute;left:71px;top:597px;width:550px;font-size:12.1px;line-height:24px;text-align:justify}
.feature{position:absolute;left:639px;top:554px;width:297px;height:199px;background:#e8ebee;padding:9px}
.feature .photo,.thumb .photo{width:100%;height:100%;background:linear-gradient(180deg,#b9cbe0,#6f7886 60%,#4a4440)}
.service{position:absolute;font-size:12px;line-height:18px;text-align:justify}
.thumb{position:absolute;background:#e8ebee;padding:6px}
.gallery-strip{position:absolute;left:482px;top:829px;display:flex;gap:7px;align-items:center}
.gallery-strip .thumb{position:static;width:81px;height:74px;padding:5px;border:1px solid var(--thumb-border)}
.arrow{width:0;height:0;border-top:6px solid transparent;border-bottom:6px solid transparent}
.arrow.prev{border-right:8px solid #111;margin-right:1px}
.arrow.next{border-left:8px solid #111}
.map{position:absolute;left:484px;top:965px;width:154px;height:141px;background:#2f353e;padding:6px}
.map .photo{width:100%;height:100%;background:linear-gradient(135deg,#f1efe9,#e6e2d6 55%,#f4e58a)}
.contact{position:absolute;left:649px;top:973px;width:300px;font-size:12.7px;line-height:24.5px}
.contact dt{position:absolute;left:0;font-weight:500}
.contact dd{margin-left:81px}
.contact .cont{display:block;padding-left:5px}
.site-footer{position:absolute;left:0;top:1138px;width:1000px;height:62px;background:var(--footer)}
.foot-nav{position:absolute;left:66px;top:22px;display:flex;gap:31px}
.foot-nav a{font-size:13px;color:var(--nav);text-decoration:none}
.social{position:absolute;left:862px;top:16px;display:flex;gap:8px}
.social span{width:22px;height:22px;border-radius:3px;background:#4d8fc9}
.copyright{position:absolute;right:58px;top:45px;font-size:11px;color:#8d98a8}
</style>
</head>
<body>
<div class="stage-band"></div>
<header class="site-header">
  <div class="brand">Vexborn Platforms Ltd</div>
  <nav class="main-nav">
    <a class="active" href="#">Home</a><a href="#">Service</a><a href="#">Hoists</a><a href="#">Examples</a><a href="#">FallArescue</a><a href="#">Mast Cliber</a><a href="#">Contact Us</a>
  </nav>
</header>

<section class="slider"><div class="photo" role="img" aria-label="Scaffolding tower beside a building with workers on the roof against a grey sky"></div></section>

<main class="panel"></main>
<div class="dots"><span></span><span></span><span class="on"></span><span></span></div>

<h2 style="left:70px;top:562px">Welcome To Our Website</h2>
<p class="intro">Lorem Ipsum is simply dummy text of the printing and typesetting industry. Lorem Ipsum has been the industry's standard dummy text ever since the 1500s, when an unknown printer took a galley of type and scrambled it to make a type specimen book. It has survived not only five centuries, but also the leap into electronic typesetting, remaining essentially unchanged. It was popularised in the 1960s with the release of Tessaform sheets containing Lorem Ipsum passages, and more recently with desktop publishing software like Quarlo LayoutDesk including versions of Lorem Ipsum.</p>
<figure class="feature"><div class="photo" role="img" aria-label="Steel truss bridge on brick piers under a blue sky"></div></figure>

<h2 style="left:69px;top:772px">Services</h2>
<figure class="thumb" style="left:72px;top:817px;width:108px;height:98px"><div class="photo" role="img" aria-label="Access platform mounted on a building facade"></div></figure>
<p class="service" style="left:191px;top:825px;width:256px">There are many variations of passages of Lorem Ipsum available, but the majority have suffered alteration in some form, by injected humour, or randomised words which don't look even slightly believable</p>
<p class="service" style="left:72px;top:928px;width:256px">There are many variations of passages of Lorem Ipsum available, but the majority have suffered alteration in some form, by injected humour, or randomised words which don't look even slightly believable</p>
<figure class="thumb" style="left:339px;top:928px;width:108px;height:97px"><div class="photo" role="img" aria-label="Steel bridge section seen from below"></div></figure>
<figure class="thumb" style="left:69px;top:1031px;width:108px;height:98px"><div class="photo" role="img" aria-label="Underside of a steel bridge with suspended cradle"></div></figure>
<p class="service" style="left:191px;top:1038px;width:256px">There are many variations of passages of Lorem Ipsum available, but the majority have suffered alteration in some form, by injected humour, or randomised words which don't look even slightly believable</p>

<h2 style="left:487px;top:782px">Gallery</h2>
<div class="gallery-strip">
  <span class="arrow prev"></span>
  <figure class="thumb"><div class="photo" role="img" aria-label="Steel truss bridge"></div></figure>
  <figure class="thumb"><div class="photo" role="img" aria-label="Bridge piers and deck"></div></figure>
  <figure class="thumb"><div class="photo" role="img" aria-label="Platform on a building"></div></figure>
  <figure class="thumb"><div class="photo" role="img" aria-label="Bridge underside with cradle"></div></figure>
  <figure class="thumb"><div class="photo" role="img" aria-label="Worker in hard hat on site" style="background:linear-gradient(180deg,#c9a66b,#7a5a34)"></div></figure>
  <span class="arrow next"></span>
</div>

<h2 style="left:489px;top:923px">Contact Us</h2>
<figure class="map"><div class="photo" role="img" aria-label="Street map showing the office location"></div></figure>
<dl class="contact">
  <dt>Address</dt><dd>: There are many variations of<span class="cont">passages of Lorem Ipsum available,</span></dd>
  <dt>Office Phone</dt><dd>: (005) 317 4920</dd>
  <dt>Fax</dt><dd>: (008) 642 1093</dd>
  <dt>E-mail</dt><dd>: info@vexborn.com</dd>
</dl>

<footer class="site-footer">
  <nav class="foot-nav"><a href="#">Home</a><a href="#">Service</a><a href="#">Hoists</a><a href="#">Examples</a><a href="#">FallArescue</a><a href="#">Mast Cliber</a><a href="#">Contact Us</a></nav>
  <div class="social"><span aria-label="Social link"></span><span aria-label="Social link"></span><span aria-label="Social link"></span></div>
  <p class="copyright">Copyright © 2011. www.vexbornplatforms.com</p>
</footer>
</body>
</html>
```